Boutique custom software development company needs new business card

Our nearly 20 year old custom software development company would like to better include the fact that we are now providing Bitcoin services. These new services are B2B include education (how to acquire and securely hold Bitcoin) and integrating Bitcoin payments into existing ecommerce sites or other existing systems. Please keep the card clean and simple. Attached is our current design and some other files. velquor.example

Target Market(s)

businesses owners interested in long term relationship

Industry/Entity Type

Custom software development and Bitcoin

Contact Information for Business Card

Dale Furness, dale@velquor.example, velquor.example, (555) 274-VELQ

Font styles to use
Other font styles liked:
• monospace

Requirements
Must have
• double-sided
Nice to have
• clean and simple
Should not have
• physical address

```html
<!DOCTYPE html>
<html lang="en">
<head>
<meta charset="utf-8">
<title>Velquor Business Card</title>
<link rel="stylesheet" href="https://fonts.googleapis.com/css2?family=Montserrat:wght@500;600;700&family=Lato:wght@400&display=swap">
<style>
  :root {
    --page-bg: #161616;
    --card-bg: #262626;
    --card-edge: #1f1f1f;
    --brand-blue: #3b78c4;
    --brand-orange: #f07f22;
    --text-light: #f2f2f2;
  }
  * { box-sizing: border-box; margin: 0; padding: 0; }
  html, body {
    width: 1200px; height: 900px; overflow: hidden;
    background: var(--page-bg);
  }
  .canvas {
    position: relative; width: 1200px; height: 900px;
    display: flex; flex-direction: column; align-items: center; justify-content: center; gap: 36px;
  }
  .card {
    width: 630px; height: 360px;
    background: radial-gradient(ellipse at 80% 30%, #2e2e2e 0%, var(--card-bg) 55%, var(--card-edge) 100%);
    box-shadow: 0 14px 30px rgba(0,0,0,.6);
    position: relative;
  }
  .wordmark {
    font-family: 'Montserrat', sans-serif; font-weight: 700;
    color: var(--brand-blue); letter-spacing: 1px; line-height: 1;
    display: flex; align-items: center; gap: 12px; white-space: nowrap;
  }
  .wordmark-dot {
    flex: none;
    width: 0.55em; height: 0.55em; border-radius: 50%;
    background: var(--brand-orange); display: inline-block;
  }
  .tagline {
    font-family: 'Lato', sans-serif; font-weight: 400;
    color: var(--brand-blue); letter-spacing: -0.3px; white-space: nowrap;
  }
  .services {
    font-family: 'Lato', sans-serif; font-weight: 400;
    color: var(--brand-orange); white-space: nowrap;
  }
  /* front */
  .card-front { display: flex; flex-direction: column; align-items: center; justify-content: center; }
  .card-front .wordmark { font-size: 64px; }
  .card-front .tagline { font-size: 22px; margin-top: 8px; }
  .card-front .services { font-size: 17px; margin-top: 6px; }
  /* back */
  .card-back { display: flex; align-items: center; padding: 0 30px 0 36px; }
  .brand-block { width: 270px; flex: none; }
  .card-back .wordmark { font-size: 44px; gap: 10px; }
  .card-back .tagline { font-size: 16px; margin-top: 8px; }
  .card-back .services { font-size: 13.5px; margin-top: 4px; }
  .divider { width: 2px; height: 170px; background: var(--brand-orange); margin: 0 24px 0 16px; flex: none; }
  .contact-block { font-family: 'Montserrat', sans-serif; color: var(--text-light); }
  .person-name { font-size: 21px; font-weight: 600; letter-spacing: 1.2px; text-transform: uppercase; white-space: nowrap; }
  .person-name .first { color: var(--brand-orange); }
  .person-name .last { color: var(--brand-blue); }
  .person-role { font-size: 14px; font-weight: 500; letter-spacing: 1.2px; margin: 2px 0 14px; }
  .contact-line { display: flex; align-items: center; gap: 8px; font-size: 14.5px; font-weight: 500; line-height: 1.6; white-space: nowrap; }
  .contact-line svg { width: 13px; height: 13px; flex: none; }
  .web-domain { color: var(--brand-blue); }
</style>
</head>
<body>
<main class="canvas">
  <section class="card card-front">
    <div class="wordmark"><span class="wordmark-dot"></span>VELQUOR</div>
    <p class="tagline">developer of custom applications</p>
    <p class="services">Bitcoin payments &amp; education</p>
  </section>

  <section class="card card-back">
    <div class="brand-block">
      <div class="wordmark"><span class="wordmark-dot"></span>VELQUOR</div>
      <p class="tagline">developer of custom applications</p>
      <p class="services">Bitcoin payments &amp; education</p>
    </div>
    <div class="divider"></div>
    <div class="contact-block">
      <p class="person-name"><span class="first">Dale</span> <span class="last">Furness</span></p>
      <p class="person-role">DIRECTOR</p>
      <p class="contact-line">
        <svg viewBox="0 0 16 16"><path d="M3 1.5l2.5-.5 1.5 3.5-1.8 1.2a8 8 0 0 0 4 4l1.2-1.8 3.5 1.5-.5 2.5c-.3 1-1 1.6-2 1.6C6 13.5 1.5 9 1.5 3.5c0-1 .6-1.7 1.5-2z" fill="var(--brand-orange)"/></svg>
        (555) 274-VELQ
      </p>
      <p class="contact-line">
        <svg viewBox="0 0 16 16"><rect x="1.5" y="3.5" width="13" height="9" fill="none" stroke="var(--brand-orange)" stroke-width="1.4"/><path d="M1.5 3.5 8 9l6.5-5.5" fill="none" stroke="var(--brand-orange)" stroke-width="1.4"/></svg>
        dale@velquor.example
      </p>
      <p class="contact-line">
        <svg viewBox="0 0 16 16"><circle cx="8" cy="8" r="6.5" fill="none" stroke="var(--brand-orange)" stroke-width="1.3"/><ellipse cx="8" cy="8" rx="2.8" ry="6.5" fill="none" stroke="var(--brand-orange)" stroke-width="1.1"/><path d="M1.5 8h13M2.5 5h11M2.5 11h11" stroke="var(--brand-orange)" stroke-width="1"/></svg>
        <span>www.<span class="web-domain">velquor</span>.example</span>
      </p>
    </div>
  </section>
</main>
</body>
</html>
```